High End Art Gallery Business Card

We're looking for a business card design that is elegant and artful. Foil embossing, blind embossed pattern, or some kind of "extra" element to make it stand out. Standard American size. The back should remain blank or nearly blank so that notes can be written on the back.
Please check our website at lenakellerby.com to see information about our gallery and the type of artwork that we sell.
Included with the files is a brand identity guideline. In addition to the colors listed, we like to incorporate an indigo blue. The business card design in the guideline seems too simplistic. I have included some photos of other business card designs that have caught my eye.
thank you!

Contact Information for Business Card

Nadia Kellerby
Gallery Owner
remaining details are in the attached docs

Requirements
Nice to have
• some kind of natural/organic element to reflect the hand-made nature of all of the original artwork.

```html
<!DOCTYPE html>
<html lang="en">
<head>
<meta charset="utf-8">
<title>Kellerby Gallery — Business Cards</title>
<link href="https://fonts.googleapis.com/css2?family=Marcellus&family=Roboto:wght@400&display=swap" rel="stylesheet">
<style>
  :root {
    --navy: #0f2a57;
    --navy-deep: #0b2250;
    --gold: #c9a24a;
    --ink: #1b2f5a;
    --paper: #ffffff;
    --edge: #d4d4d4;
    --note-red: #c8373a;
  }
  html, body {
    margin: 0;
    padding: 0;
    width: 1200px;
    height: 1200px;
    overflow: hidden;
    background: var(--paper);
  }
  .board { position: relative; width: 1200px; height: 1200px; }
  .card { position: absolute; box-sizing: border-box; overflow: hidden; }
  .card--front {
    background: radial-gradient(ellipse at 30% 50%, var(--navy) 0%, var(--navy-deep) 100%);
  }
  .card--back { background: var(--paper); border: 2px solid var(--edge); }
  .card--raised { box-shadow: 10px 12px 14px rgba(0,0,0,0.32); }

  .brand-dot {
    position: absolute;
    border-radius: 50%;
    box-sizing: border-box;
    border: 6px solid var(--gold);
  }
  .brand-name {
    position: absolute;
    color: var(--gold);
    font-family: "Roboto", sans-serif;
    font-weight: 400;
    white-space: nowrap;
    line-height: 1;
    letter-spacing: 0.08em;
  }
  .brand-tagline {
    position: absolute;
    color: var(--gold);
    font-family: "Roboto", sans-serif;
    font-weight: 400;
    white-space: nowrap;
    line-height: 1;
    letter-spacing: 0.2em;
  }

  .contact { position: absolute; color: var(--ink); white-space: nowrap; line-height: 1; }
  .contact .name { position: absolute; left: 0; font-family: "Marcellus", serif; letter-spacing: 0.04em; }
  .contact .role { position: absolute; left: 0; font-family: "Roboto", sans-serif; letter-spacing: 0.1em; }
  .contact .line { position: absolute; left: 0; font-family: "Roboto", sans-serif; }
  .contact b { font-weight: 400; margin-right: 0.45em; }

  /* large top pair */
  .card-a-back { left: 132px; top: 362px; width: 664px; height: 378px; }
  .card-a-front { left: 417px; top: 93px; width: 663px; height: 379px; }
  .card-a-front .brand-dot { left: 35px; top: 103px; width: 172px; height: 172px; }
  .card-a-front .brand-name { left: 239px; top: 170px; font-size: 32px; }
  .card-a-front .brand-tagline { left: 240px; top: 222px; font-size: 13px; }
  .card-a-back .contact { left: 46px; top: 0; }
  .card-a-back .name { top: 44px; font-size: 22px; }
  .card-a-back .role { top: 80px; font-size: 15px; }
  .card-a-back .line { font-size: 20px; }

  /* small bottom pair */
  .card-b-front { left: 135px; top: 834px; width: 469px; height: 268px; }
  .card-b-back { left: 622px; top: 834px; width: 469px; height: 268px; }
  .card-b-front .brand-dot { left: 25px; top: 73px; width: 122px; height: 122px; border-width: 4px; }
  .card-b-front .brand-name { left: 169px; top: 120px; font-size: 23px; }
  .card-b-front .brand-tagline { left: 170px; top: 157px; font-size: 9px; }
  .card-b-back .contact { left: 32px; top: 0; }
  .card-b-back .name { top: 32px; font-size: 16px; }
  .card-b-back .role { top: 57px; font-size: 11px; }
  .card-b-back .line { font-size: 14px; }
  .handwritten-note {
    position: absolute; left: 238px; top: 46px; width: 194px; height: 168px;
    background: linear-gradient(135deg, rgba(200,55,58,0.12), rgba(200,55,58,0.05));
    border-radius: 4px;
  }
</style>
</head>
<body>
<main class="board">

  <section class="card card--back card--raised card-a-back">
    <div class="contact">
      <div class="name">NADIA KELLERBY</div>
      <div class="role">CO-OWNER</div>
      <div class="line" style="top:128px"><b>T</b>808-555-0147</div>
      <div class="line" style="top:157px"><b>F</b>808-555-0192</div>
      <div class="line" style="top:186px">info@lenakellerby.com</div>
      <div class="line" style="top:223px">412 Makai Lane</div>
      <div class="line" style="top:252px">Honolulu, Hawai‘i 96801</div>
      <div class="line" style="top:291px">lenakellerby.com</div>
    </div>
  </section>

  <section class="card card--front card--raised card-a-front">
    <div class="brand-dot"></div>
    <div class="brand-name">KELLERBY GALLERY</div>
    <div class="brand-tagline">CURATED WORKS FROM THE ISLANDS</div>
  </section>

  <section class="card card--front card-b-front">
    <div class="brand-dot"></div>
    <div class="brand-name">KELLERBY GALLERY</div>
    <div class="brand-tagline">CURATED WORKS FROM THE ISLANDS</div>
  </section>

  <section class="card card--back card-b-back">
    <div class="contact">
      <div class="name">NADIA KELLERBY</div>
      <div class="role">CO-OWNER</div>
      <div class="line" style="top:92px"><b>T</b>808-555-0147</div>
      <div class="line" style="top:112px"><b>F</b>808-555-0192</div>
      <div class="line" style="top:132px">info@lenakellerby.com</div>
      <div class="line" style="top:159px">412 Makai Lane</div>
      <div class="line" style="top:180px">Honolulu, Hawai‘i 96801</div>
      <div class="line" style="top:207px">lenakellerby.com</div>
    </div>
    <div class="handwritten-note" role="img" aria-label="Handwritten note in red ink naming an artwork, its artist and a price range"></div>
  </section>

</main>
</body>
</html>
```